Velvora Style & Image Consultancy

Hi, I need a brochure design for my personal styling business. I have downloaded the company logo along with the content of the services offered for the brochure. Being a colour and styling business I would been keen on having some pictures of timeless fashion or colour samples, This is not absolutely necessary just an idea. I had also thought about changing and naming the services offered with a feminine, fun interesting type of theme. This may make it more inviting, I would be really interested in any of your creative ideas in this area. I will be deciding on the business card design in the next couple of days. I will download the design for this once I have made the decision. I will be okay to pay for any photo images that may be required if the brochure is selected. I had envisaged a tri fold brochure standard letter size with two folds (8.5" by 11inchs) however I am open to any suggestions. Please feel free to make any changes or modification's to the content, font etc in the files downloaded for the brochure. Many Thanks.
Updates
Project Deadline Extended
Reason: I need to extend the time for this project as I do not have all of content required for the brochure confirmed. Many Thanks
Industry/Entity Type
Fashion
Font styles to use
Look and feel
Each slider illustrates characteristics of the customer's brand and the style your logo design should communicate.

```html
<!DOCTYPE html>
<html lang="en">
<head>
<meta charset="utf-8">
<title>Velvora Style &amp; Image Consultancy – Brochure Spread</title>
<link href="https://fonts.googleapis.com/css2?family=Courgette&family=Questrial&display=swap" rel="stylesheet">
<style>
  :root {
    --backdrop: #5f5f61;
    --cream-light: #f6efd2;
    --cream-mid: #e9dcaa;
    --gold-deep: #cdb878;
    --espresso: #241712;
    --espresso-soft: #3a2820;
    --ink: #2b211c;
    --gold-accent: #c9a227;
    --slate: #5f5d5e;
    --slate-light: #8a8788;
    --white: #ffffff;
  }
  * { margin: 0; padding: 0; box-sizing: border-box; }
  html, body { width: 1200px; height: 626px; overflow: hidden; }
  body {
    background: var(--backdrop);
    font-family: "Questrial", "Century Gothic", sans-serif;
    color: var(--ink);
    position: relative;
  }
  .spread {
    position: absolute;
    left: 210px; top: 10px;
    width: 780px; height: 606px;
    overflow: hidden;
    background: linear-gradient(90deg, var(--cream-light) 0%, var(--cream-mid) 30%, var(--cream-light) 34%, var(--cream-mid) 58%, var(--gold-deep) 65.5%);
  }
  .cover-backdrop {
    position: absolute;
    left: 511px; top: 0; width: 269px; height: 606px;
    background:
      radial-gradient(ellipse 40% 30% at 85% 12%, rgba(214, 196, 140, 0.75) 0%, rgba(214, 196, 140, 0) 100%),
      radial-gradient(ellipse 35% 28% at 12% 30%, rgba(214, 196, 140, 0.55) 0%, rgba(214, 196, 140, 0) 100%),
      linear-gradient(180deg, #f3ecd9 0%, #f8f5ee 50%, #efe8da 100%);
  }
  .cover-photo {
    position: absolute;
    left: 560px; top: 14px; width: 180px; height: 500px;
    border-radius: 90px 90px 40px 40px;
    background:
      radial-gradient(ellipse 28% 10% at 45% 9%, #d8b27e 0%, rgba(216, 178, 126, 0) 100%),
      radial-gradient(ellipse 55% 40% at 50% 55%, #fffdf7 0%, #f4ecd9 70%, rgba(244, 236, 217, 0) 100%),
      linear-gradient(180deg, rgba(238, 228, 205, 0) 0%, #efe6d1 30%, #ece1c6 70%, #a39585 92%, rgba(163, 149, 133, 0) 100%);
  }
  .wave { position: absolute; inset: 0; width: 780px; height: 606px; }
  .panel { position: absolute; top: 0; }
  .panel--intro { left: 0; width: 258px; padding: 24px 16px 0 16px; }
  .panel--colour { left: 258px; width: 253px; padding: 24px 14px 0 18px; }
  .panel-title {
    font-family: "Courgette", cursive;
    font-weight: 400;
    font-size: 19px;
    line-height: 1.2;
    text-align: center;
    color: var(--ink);
    margin-bottom: 16px;
  }
  .panel-text { font-size: 8.6px; line-height: 1.42; margin-bottom: 11px; }
  .list-title {
    font-family: "Courgette", cursive;
    font-weight: 400;
    font-size: 11px;
    margin: 4px 0 6px;
  }
  .service-list { list-style: none; font-size: 8.6px; line-height: 1.68; }
  .service-list li::before, .discover-list li::before {
    content: ""; display: inline-block; width: 4px; height: 4px;
    border-radius: 50%; background: var(--ink);
    margin: 0 8px 1px 2px; vertical-align: middle;
  }
  .discover-list { list-style: none; font-size: 8.6px; line-height: 1.42; }
  .discover-list li { padding-left: 14px; text-indent: -14px; margin-bottom: 1px; }
  .session-title {
    font-family: "Courgette", cursive;
    font-weight: 400;
    font-size: 17px;
    margin: 30px 0 26px;
  }
  .session-text { font-size: 8.6px; line-height: 1.42; margin-bottom: 9px; }
  .photo-circle {
    position: absolute; border-radius: 50%;
    border: 4px solid var(--white);
  }
  .photo-circle--portrait {
    left: 138px; top: 300px; width: 96px; height: 96px;
    background: radial-gradient(circle at 50% 45%, #e8b98f 0%, #a8674c 45%, #5a3d35 100%);
  }
  .photo-circle--shoes {
    left: 8px; top: 428px; width: 132px; height: 132px;
    background: linear-gradient(90deg, #d9df3a 0%, #e0a53b 30%, #c8328f 60%, #b8283d 85%, #9fb8bf 100%);
  }
  .photo-circle--car {
    left: 172px; top: 464px; width: 84px; height: 84px;
    background: linear-gradient(180deg, #d9d4c6 0%, #9fc0c4 55%, #6d7f80 100%);
  }
  .medallion { position: absolute; border-radius: 50%; background: var(--slate); }
  .medallion--back { left: 344px; top: 508px; width: 44px; height: 44px; }
  .medallion--cover { left: 588px; top: 318px; width: 90px; height: 90px; }
  .brand {
    position: absolute; left: 578px; top: 520px;
    display: flex; align-items: center; gap: 10px;
    color: var(--slate-light);
  }
  .brand-mark {
    width: 30px; height: 30px; border-radius: 50%;
    background: var(--slate-light);
    flex: none;
  }
  .brand-text { display: flex; flex-direction: column; }
  .brand-name { font-size: 30px; line-height: 1; letter-spacing: 0.5px; }
  .brand-tagline { font-size: 8px; margin-top: 4px; letter-spacing: 0.3px; }
</style>
</head>
<body>
  <main class="spread">
    <div class="cover-backdrop" role="img" aria-label="Soft cream background with pale gold flourishes"></div>
    <div class="cover-photo" role="img" aria-label="Photograph of a woman in a white sleeveless dress with a full skirt and grey heeled sandals"></div>

    <svg class="wave" viewBox="0 0 780 606" aria-hidden="true">
      <path d="M0,392 C90,440 200,500 330,505 C430,510 520,500 600,470 C680,440 740,410 780,378 L780,606 L0,606 Z" fill="var(--espresso)"/>
      <path d="M0,392 C90,440 200,500 330,505 C430,510 520,500 600,470 C680,440 740,410 780,378" fill="none" stroke="var(--espresso-soft)" stroke-width="3"/>
    </svg>

    <section class="panel panel--intro">
      <h1 class="panel-title">Dress For The Life<br>You Love</h1>
      <p class="panel-text">Time for a change, take a fresh look and discover how to dress in a style that reflects your personality &amp; lifestyle. Be confident, look amazing &amp; feel great about the way that you look every day.</p>
      <p class="panel-text">Be empowered and understand how you can dress for success everyday. Discover the elements in creating an overall balance and harmony in putting together a stylish functional wardrobe that reflects you and your lifestyle.</p>
      <h2 class="list-title">Personal Styling Services</h2>
      <ul class="service-list">
        <li>Colour Analysis</li>
        <li>Image &amp; Style Consultation</li>
        <li>Wardrobe Make over</li>
        <li>Style Me Complete</li>
        <li>Personal Shopping</li>
        <li>Make up Lessons</li>
        <li>Special Occasion Make up</li>
        <li>Seasonal Review &amp; Update</li>
        <li>Party &amp; Group Experiences</li>
        <li>Complete Makeovers</li>
        <li>Personal Styling Packages</li>
      </ul>
    </section>

    <div class="photo-circle photo-circle--portrait" role="img" aria-label="Photograph of a surprised woman with curled hair against a patterned wall"></div>
    <div class="photo-circle photo-circle--shoes" role="img" aria-label="Photograph of a row of colourful high-heeled shoes on a shelf"></div>
    <div class="photo-circle photo-circle--car" role="img" aria-label="Photograph of a pale blue vintage car"></div>

    <section class="panel panel--colour">
      <h2 class="panel-title">Velvora Color<br>Consultation</h2>
      <p class="panel-text">Colour has a huge impact on the way we look and how we feel. Wearing colours that compliment us help us appear vibrant; your eyes will sparkle, giving you a more youthful and healthier appearance.</p>
      <p class="panel-text">During an individual colour consultation you will discover</p>
      <ul class="discover-list">
        <li>What your dominant colouring or season is, which colours suit you.</li>
        <li>How to select colour for garments to enhance your colouring and flatter your body shape.</li>
        <li>How to select and wear colours to suit your personality and lifestyle.</li>
        <li>How to coordinate &amp; wear colours in your wardrobe.</li>
        <li>With a make- up makeover, what makeup colours and shades to select to flatter your colouring, and keep your look current.</li>
      </ul>
      <h3 class="session-title">Session:</h3>
      <p class="session-text">Duration – 1 hour 30mins to 2 hours<br>Includes – Takeaway a colour swatch of your best colours.</p>
      <p class="session-text">Information workbook with personalised notes discussed during the consultation.</p>
      <p class="session-text">Cost: $225.00</p>
    </section>

    <div class="medallion medallion--back"></div>
    <div class="medallion medallion--cover"></div>

    <div class="brand">
      <span class="brand-mark"></span>
      <span class="brand-text">
        <span class="brand-name">Velvora</span>
        <span class="brand-tagline">Style &amp; Image Consultancy</span>
      </span>
    </div>
  </main>
</body>
</html>
```